Tasman Curdworks Guild needs new business cards

We need new business cards designed and produced. We are likely to need other design work done for ads, flyers etc in future.

We would like to start with an initial business card.

The Tasman Curdworks Guild (TCG) is a membership-based not-for-profit organisation that looks after the interests of Australia's small to medium artisan cheesemakers, many of whom are also small-scale farmers. The design should be simple, using our logo, but also communicate our artisan cheese and small dairy farm focus.

The first card to be designed and produced is for me, Miriam Tolhurst. My details are:

Miriam Tolhurst
Secretary
Tasman Curdworks Guild (TCG)
http://www.curdworksguild.example
T +61452837190
E miriam.miriamtolhurst@mailbox.example

I have attached the TCG logo in jpg form. I have a higher resolution version available if needed.

Thank you!

Miriam

Miriam Tolhurst
Tasman Curdworks Guild
miriam.miriamtolhurst@mailbox.example
+61452837190

Sans Serif

• Logo (see attached file)

```html
<!DOCTYPE html>
<html lang="en">
<head>
<meta charset="utf-8">
<title>Tasman Curdworks Guild – Business Card</title>
<link href="https://fonts.googleapis.com/css2?family=Open+Sans:wght@400;600&display=swap" rel="stylesheet">
<style>
  :root {
    --backdrop: #c5c4c5;
    --card: #2a2a2a;
    --gold: #f1c35e;
  }
  * { margin: 0; padding: 0; box-sizing: border-box; }
  html, body {
    width: 1200px;
    height: 1000px;
    overflow: hidden;
    background: var(--backdrop);
    font-family: "Open Sans", Arial, sans-serif;
  }
  .business-card {
    position: absolute;
    left: 150px;
    top: 240px;
    width: 900px;
    height: 520px;
    background: var(--card);
    border-radius: 44px;
    color: var(--gold);
  }
  .guild-mark {
    position: absolute;
    top: 62px;
    right: 70px;
    display: flex;
    align-items: center;
    gap: 22px;
  }
  .guild-mark__dot {
    width: 78px;
    height: 78px;
    border-radius: 50%;
    background: var(--gold);
    flex: none;
  }
  .guild-mark__name {
    font-size: 27px;
    font-weight: 400;
    line-height: 1.2;
    width: 190px;
  }
  .holder {
    position: absolute;
    left: 66px;
    bottom: 62px;
  }
  .holder__name {
    font-size: 33px;
    font-weight: 600;
    text-transform: uppercase;
    letter-spacing: 0.5px;
    line-height: 1.1;
  }
  .holder__role {
    font-size: 20px;
    font-weight: 600;
    text-transform: uppercase;
    margin: 4px 0 0 18px;
  }
  .holder__rule {
    width: 118px;
    height: 2px;
    background: var(--gold);
    margin: 10px 0 22px 18px;
  }
  .contact-list {
    list-style: none;
    margin-left: 18px;
    font-size: 19px;
    line-height: 1.55;
  }
</style>
</head>
<body>
  <main class="business-card">
    <div class="guild-mark">
      <span class="guild-mark__dot"></span>
      <span class="guild-mark__name">Tasman Curdworks Guild</span>
    </div>

    <section class="holder">
      <h1 class="holder__name">Miriam Tolhurst</h1>
      <p class="holder__role">Secretary</p>
      <div class="holder__rule"></div>
      <ul class="contact-list">
        <li>P: +61452837190</li>
        <li>E: miriam.miriamtolhurst@mailbox.example</li>
        <li>W: www.curdworksguild.example</li>
      </ul>
    </section>
  </main>
</body>
</html>
```